Attorney Business Card

I need a business card that looks professional yet modern. I am an Attorney. , I need a professional yet modern business card for my law practice. My logo and information have been uploaded. , I need a business card that looks professional yet modern. I am an Attorney. , I need a professional yet modern business card for my law practice. My logo and information have been uploaded.

Industry/Entity Type

Business

Requirements
Must have
• My logo which has been uploaded , my logo , My logo which has been uploaded , my logo

```html
<!DOCTYPE html>
<html lang="en">
<head>
<meta charset="utf-8">
<title>Varessi Law Firm – Business Card</title>
<link rel="stylesheet" href="https://fonts.googleapis.com/css2?family=Montserrat:wght@800&family=Questrial&display=swap">
<style>
  :root {
    --backdrop: #2b2b2e;
    --purple-light: #5a2870;
    --purple-mid: #43195a;
    --purple-dark: #2a0f38;
    --accent-blue: #2aa9e0;
    --accent-orange: #f39a1e;
    --watermark: rgba(140, 110, 170, 0.16);
  }
  * { box-sizing: border-box; margin: 0; padding: 0; }
  html, body { width: 1200px; height: 900px; overflow: hidden; }
  body {
    background: var(--backdrop);
    display: flex;
    flex-direction: column;
    align-items: center;
    justify-content: center;
    gap: 40px;
    font-family: "Questrial", "Century Gothic", sans-serif;
  }
  .card {
    position: relative;
    width: 630px;
    height: 360px;
    overflow: hidden;
    border-radius: 4px;
    background: radial-gradient(ellipse at 45% 30%, var(--purple-light) 0%, var(--purple-mid) 50%, var(--purple-dark) 100%);
    box-shadow: 0 10px 30px rgba(0,0,0,0.45);
  }
  .brand {
    display: flex;
    align-items: center;
    gap: 14px;
    color: var(--accent-blue);
    font-family: "Questrial", "Century Gothic", sans-serif;
    letter-spacing: 0.08em;
    text-transform: uppercase;
    white-space: nowrap;
  }
  .brand-dot {
    flex: none;
    border: 4px solid var(--accent-blue);
    border-radius: 50%;
  }
  /* Front */
  .card-front { display: flex; align-items: center; justify-content: center; }
  .card-front .brand { font-size: 40px; }
  .card-front .brand-dot { width: 86px; height: 86px; }
  /* Back */
  .watermark {
    position: absolute;
    left: 190px;
    top: 40px;
    display: flex;
    flex-direction: column;
    align-items: center;
    color: var(--watermark);
    font-size: 72px;
    letter-spacing: 0.06em;
    text-transform: uppercase;
    pointer-events: none;
  }
  .watermark-ring {
    width: 150px; height: 150px;
    border: 6px solid var(--watermark);
    border-radius: 50%;
    margin-bottom: 10px;
  }
  .card-back .brand {
    position: absolute;
    left: 34px;
    top: 150px;
    font-size: 19px;
    gap: 10px;
  }
  .card-back .brand-dot { width: 56px; height: 56px; border-width: 3px; }
  .holder { position: absolute; left: 330px; top: 30px; }
  .holder-name {
    font-family: "Montserrat", "Arial Black", sans-serif;
    font-weight: 800;
    font-size: 17px;
    color: var(--accent-orange);
    text-transform: uppercase;
  }
  .holder-title { font-size: 18px; color: var(--accent-orange); margin-top: 2px; }
  .numbers {
    position: absolute;
    left: 420px;
    top: 108px;
    color: var(--accent-orange);
    font-size: 15px;
    line-height: 1.45;
  }
  .numbers dt { display: inline-block; width: 42px; }
  .numbers dd { display: inline; }
  .numbers dd::after { content: "\A"; white-space: pre; }
  .web { position: absolute; right: 26px; top: 232px; color: var(--accent-orange); font-size: 15px; }
  .address {
    position: absolute;
    left: 30px;
    bottom: 22px;
    color: var(--accent-orange);
    font-size: 16px;
    letter-spacing: 0.04em;
    text-transform: uppercase;
  }
</style>
</head>
<body>
  <section class="card card-front" aria-label="Card front">
    <div class="brand"><span class="brand-dot"></span>Varessi Law Firm</div>
  </section>

  <section class="card card-back" aria-label="Card back">
    <div class="watermark" aria-hidden="true">
      <span class="watermark-ring"></span>
      <span>Varessi</span>
    </div>
    <div class="brand"><span class="brand-dot"></span>Varessi Law Firm</div>
    <div class="holder">
      <p class="holder-name">Daniel Varessi, Esq.</p>
      <p class="holder-title">Attorney At LAW</p>
    </div>
    <dl class="numbers">
      <dt>Tel</dt><dd>:555.014.2200</dd>
      <dt>Fax</dt><dd>:555.014.2210</dd>
      <dt>Mob</dt><dd>:555.017.3344</dd>
    </dl>
    <p class="web">daniel@vlfirm.com / www.vlfirm.com</p>
    <p class="address">1820 Harbor View Ave. Suite 900, Lakemont, CA 90471</p>
  </section>
</body>
</html>
```